Presentation Folder, Business Card, Letterhead and Envelope design

We are a dental clinic that will open in August and we are looking for a professional graphic designer to create our Business Card, Presentation Folder, Letterhead, Notepad and envelopes.

The brand NovaGrin must reflect a sense of quality and sophistication, marketed for middle-class consumers.
Our preference is for quality and refined materials, where less is more.
Attached the logo

```html
<!DOCTYPE html>
<html lang="en">
<head>
<meta charset="utf-8">
<title>NovaGrin — Stationery Set</title>
<link rel="stylesheet" href="https://fonts.googleapis.com/css2?family=Montserrat:wght@300;500&family=Poppins:wght@400;500&display=swap">
<style>
  :root{
    --bg:#e8e8e9;
    --paper:#f6f6f6;
    --wine:#5e0e10;
    --graphite:#58595b;
    --rule-grey:#9a9a9c;
    --ink:#3b3b3d;
    --logo-font:'Montserrat', sans-serif;
    --text-font:'Poppins', sans-serif;
  }
  *{box-sizing:border-box;margin:0;padding:0}
  html,body{width:1200px;height:857px;overflow:hidden;background:var(--bg)}
  .canvas{position:relative;width:1200px;height:857px}

  .sheet{position:absolute;background:var(--paper);box-shadow:0 2px 6px rgba(0,0,0,.12);overflow:hidden}

  /* brand lockup */
  .brand{display:flex;align-items:center;gap:.5em;font-family:var(--logo-font);font-weight:300;color:var(--graphite);letter-spacing:.32em;text-transform:uppercase;line-height:1}
  .brand-mark{width:.95em;height:.95em;background:var(--wine);flex:none}
  .brand--light{color:#fff}
  .brand--light .brand-mark{background:#fff}

  /* footer rule motif */
  .footer-rule{position:absolute;left:0;right:0;bottom:0;height:40px}
  .footer-rule .hairline{position:absolute;left:42%;right:0;bottom:14px;height:1px;background:var(--rule-grey)}
  .footer-rule .band{position:absolute;left:42%;right:0;bottom:6px;height:5px;background:var(--wine)}
  .footer-rule .url{position:absolute;right:12px;bottom:18px;font-family:var(--text-font);font-size:6.5px;color:var(--graphite);letter-spacing:.06em}

  /* contact block */
  .contact{font-family:var(--text-font);font-size:6.5px;color:var(--ink);line-height:1.55;border-left:1px solid var(--wine);padding-left:8px}
  .contact li{list-style:none;display:flex;align-items:center;gap:4px}
  .contact .ico{width:6px;height:6px;background:var(--wine);flex:none}
  .contact .indent{padding-left:10px}

  /* letterhead */
  .letterhead{left:40px;top:40px;width:350px;height:495px}
  .letterhead .brand{position:absolute;left:30px;top:78px;font-size:17px}
  .letterhead .contact{position:absolute;left:218px;top:34px}

  /* folder cover */
  .folder-cover{left:420px;top:40px;width:350px;height:495px}
  .folder-cover .brand{position:absolute;left:0;right:0;top:120px;justify-content:center;font-size:19px}

  /* folder pocket */
  .folder-pocket{left:800px;top:40px;width:360px;height:190px}
  .folder-pocket .flap{position:absolute;left:0;right:0;top:0;height:92px;background:var(--wine);border-radius:0 0 16px 16px;display:flex;align-items:center;justify-content:center}
  .folder-pocket .flap .brand{font-size:13px}

  /* envelope */
  .envelope{left:800px;top:255px;width:360px;height:180px}
  .envelope .brand{position:absolute;left:26px;top:34px;font-size:18px}
  .envelope .contact{position:absolute;left:120px;top:94px}

  /* business cards */
  .card{width:240px;height:137px;top:580px}
  .card-front{left:40px;background:var(--wine);display:flex;align-items:center;justify-content:center}
  .card-front .brand{font-size:14px}
  .card-back{left:310px}
  .card-back .brand{position:absolute;left:18px;top:20px;font-size:12px}
  .card-back .person{position:absolute;left:18px;top:46px;font-family:var(--text-font)}
  .card-back .person-name{font-size:8px;font-weight:500;color:var(--ink);letter-spacing:.04em}
  .card-back .person-role{font-size:6px;color:var(--wine)}
  .card-back .address{position:absolute;left:18px;top:70px;font-family:var(--text-font);font-size:5.5px;color:var(--ink);line-height:1.5}
  .card-back .contact{position:absolute;left:18px;top:92px;border-left:none;padding-left:0;font-size:5.5px}
  .card-back .contact .ico{width:5px;height:5px}
  .card-back .footer-rule .url{font-size:5px}

  /* notepad */
  .notepad{left:800px;top:465px;width:270px;height:360px}
  .notepad .spiral{position:absolute;left:6px;top:12px;bottom:12px;width:10px;display:flex;flex-direction:column;justify-content:space-between}
  .notepad .spiral span{display:block;width:8px;height:8px;border:2px solid #4a4a4c;border-radius:50%}
  .notepad .brand{position:absolute;left:52px;top:54px;font-size:13px}
  .notepad .footer-rule .url{font-size:5.5px}
</style>
</head>
<body>
<main class="canvas">

  <section class="sheet letterhead" aria-label="Letterhead">
    <div class="brand"><span class="brand-mark"></span>NovaGrin</div>
    <ul class="contact">
      <li><span class="ico"></span>555-201-4480</li>
      <li><span class="ico"></span>555-201-4480</li>
      <li><span class="ico"></span>hello@novagrinmail.com</li>
      <li><span class="ico"></span>48 Harbour Road, Suite 210</li>
      <li class="indent">West Lane, ON, K2P 4R8</li>
    </ul>
    <div class="footer-rule"><span class="hairline"></span><span class="band"></span><span class="url">www.NOVAGRINDENTAL.com</span></div>
  </section>

  <section class="sheet folder-cover" aria-label="Presentation folder cover">
    <div class="brand"><span class="brand-mark"></span>NovaGrin</div>
    <div class="footer-rule"><span class="hairline"></span><span class="band"></span><span class="url">www.NOVAGRINDENTAL.com</span></div>
  </section>

  <section class="sheet folder-pocket" aria-label="Presentation folder pocket">
    <div class="flap"><div class="brand brand--light"><span class="brand-mark"></span>NovaGrin</div></div>
  </section>

  <section class="sheet envelope" aria-label="Envelope">
    <div class="brand"><span class="brand-mark"></span>NovaGrin</div>
    <ul class="contact">
      <li><span class="ico"></span>555-201-4480</li>
      <li><span class="ico"></span>555-201-4480</li>
      <li><span class="ico"></span>hello@novagrinmail.com</li>
      <li><span class="ico"></span>48 Harbour Road, Suite 210</li>
      <li class="indent">West Lane, ON, K2P 4R8</li>
    </ul>
    <div class="footer-rule"><span class="hairline"></span><span class="band"></span><span class="url">www.NOVAGRINDENTAL.com</span></div>
  </section>

  <section class="sheet card card-front" aria-label="Business card front">
    <div class="brand brand--light"><span class="brand-mark"></span>NovaGrin</div>
  </section>

  <section class="sheet card card-back" aria-label="Business card back">
    <div class="brand"><span class="brand-mark"></span>NovaGrin</div>
    <div class="person">
      <p class="person-name">ELENA MARSH</p>
      <p class="person-role">Manager</p>
    </div>
    <p class="address">48 Harbour Road, Suite 210<br>West Lane, ON, K2P 4R8</p>
    <ul class="contact">
      <li><span class="ico"></span>555-201-4480</li>
      <li><span class="ico"></span>555-201-4480</li>
      <li><span class="ico"></span>hello@novagrinmail.com</li>
    </ul>
    <div class="footer-rule"><span class="hairline"></span><span class="band"></span><span class="url">www.NOVAGRINDENTAL.com</span></div>
  </section>

  <section class="sheet notepad" aria-label="Notepad">
    <div class="spiral">
      <span></span><span></span><span></span><span></span><span></span><span></span><span></span><span></span><span></span><span></span><span></span><span></span><span></span><span></span><span></span><span></span><span></span><span></span>
    </div>
    <div class="brand"><span class="brand-mark"></span>NovaGrin</div>
    <div class="footer-rule"><span class="hairline"></span><span class="band"></span><span class="url">www.NOVAGRINDENTAL.com</span></div>
  </section>

</main>
</body>
</html>
```